Seeking a beautiful packaging box for Dusk Haven - an essential oil blend (mock up provided!)

My sleep brand - Dusk Haven - is almost ready to go to market. And I need a box! Dusk Haven is a high end essential oils/sleep hygiene brand.

I need a gorgeous, classy box for our 3 sizes of essential oil product we are selling. I have a draft mockup which is to approximate size (attached), but need some help with the finishing touches and layout so it's really polished. I am looking for simple/monochrome designs using black and off white (think Norvel inspo!)

We are selling a 15mL dropper bottle and two roll ons (5ml, 10ml) of the essential oil blend. These are all amber bottles with black top. The box design will be almost identical for each, with very slight variations due to size differences.

The size of the boxes will be
15mL dropper: 30x30x95mm
10ml roller: 19x19x88mm
5ml roller: 18x18x59mm

Target Market(s)

High end/high price point product, shift workers, mums, people suffering stress and insomnia

Industry/Entity Type

Health And Wellness

Font styles to use
Serif
Sans Serif

Colors

Designer to choose only greyscale colors for use in the design.

Requirements
Must have
• I have attached a word document which includes all the necessary text:
- ingredients
- directions
- cautions
- info on essential oils/dusk haven (abbreviated on the smallest box)

Additionally:
- volume
- our website
- instagram logo/duskhavenau name
- made in australia
- recycle symbol
- 12 month open symbol
Nice to have
• I would like the boxes to be monochromatic: white or off white colour, with black logo and writing. I am open to variations on the logo (ie position of writing in relation to the circle/change of font size), but mostly need help with layout, font, direction of text, design of the blank spaces, patterns etc.
Should not have
• Colours

```html
<!DOCTYPE html>
<html lang="en">
<head>
<meta charset="utf-8">
<title>Dusk Haven – Roll On Box Dieline</title>
<link rel="stylesheet" href="https://fonts.googleapis.com/css2?family=Arimo:wght@400;700&family=Great+Vibes&family=Josefin+Sans:wght@300&family=Open+Sans:wght@400;600&family=Tinos:wght@400;700&display=swap">
<style>
  :root {
    --paper: #ffffff;
    --frame: #5a5a5a;
    --panel: #33393c;
    --tuck: #2e2e2f;
    --band: #2b2c2d;
    --cut: #b0245a;
    --fold: #2f6a86;
    --ink: #f2f2f0;
    --rule: #c9cbcc;
  }
  * { box-sizing: border-box; margin: 0; padding: 0; }
  html, body { width: 1143px; height: 1200px; overflow: hidden; background: var(--paper); }
  .artboard { position: relative; width: 1143px; height: 1200px; border: 1px solid var(--frame); }
  .dieline { position: absolute; inset: 0; }
  .panel-text { position: absolute; color: var(--ink); text-align: center; }

  .brand-name {
    font-family: "Josefin Sans", sans-serif; font-weight: 300; color: var(--ink);
    text-transform: uppercase; line-height: 1; text-align: center; letter-spacing: 0.12em;
  }

  .tuck-top { left: 358px; top: 200px; width: 172px; transform: rotate(180deg); }
  .tuck-top .brand-name { font-size: 18px; }

  .ingredients { left: 194px; top: 339px; width: 160px; font-family: "Arimo", sans-serif; font-size: 10.2px; line-height: 16.7px; }
  .ingredients h3 { font-size: 10.4px; font-weight: 700; margin-bottom: 0; }
  .care-icons { position: absolute; left: 200px; top: 590px; width: 150px; height: 52px; }

  .front-brand { left: 358px; top: 440px; width: 172px; }
  .front-brand .brand-name { font-size: 30px; line-height: 1.05; }
  .product-line { left: 358px; top: 522px; width: 172px; font-family: "Great Vibes", cursive; font-size: 19px; line-height: 24px; }
  .product-line .roll { display: flex; align-items: center; justify-content: center; gap: 6px; }
  .product-line .roll::before, .product-line .roll::after { content: ""; width: 26px; height: 1px; background: var(--ink); }
  .front-photo { position: absolute; left: 359px; top: 603px; width: 171px; height: 213px;
    background: radial-gradient(ellipse at 55% 55%, #6b6e70 0%, #4a4e51 45%, #33393c 100%); }
  .front-band { position: absolute; left: 359px; top: 816px; width: 171px; height: 54px; background: var(--band);
    font-family: "Arimo", sans-serif; font-size: 14.5px; line-height: 16.5px; color: var(--ink); text-align: center; padding-top: 9px; }

  .direction { position: absolute; left: 535px; width: 161px; border: 1px solid var(--rule);
    font-family: "Open Sans", sans-serif; font-size: 10.2px; line-height: 14.8px; letter-spacing: -0.15px;
    color: var(--ink); text-align: center; padding: 11px 0 5px; white-space: nowrap; }
  .direction h4 { position: absolute; top: -9px; left: 50%; transform: translateX(-50%); background: var(--panel);
    padding: 0 7px; font-size: 10.6px; font-weight: 600; letter-spacing: 0; }
  .inhale { top: 356px; min-height: 60px; }
  .diffuse { top: 446px; min-height: 76px; }
  .bathe { top: 550px; min-height: 48px; }
  .massage { top: 626px; min-height: 77px; }
  .caution { left: 536px; top: 731px; width: 158px; font-family: "Tinos", serif; font-size: 11.5px; line-height: 18.7px; }

  .about { left: 709px; top: 354px; width: 156px; font-family: "Tinos", serif; font-size: 11.5px; line-height: 16.4px; }
  .about hr { border: 0; border-top: 1px solid var(--rule); width: 124px; margin: 15px auto 16px; }
  .about b { font-weight: 700; }
  .about a { color: var(--ink); text-decoration: underline; }
  .about .visit { line-height: 13.5px; }
  .social { margin-top: 12px; display: flex; align-items: center; justify-content: center; gap: 3px; }
  .social .dot { width: 10px; height: 10px; border-radius: 50%; border: 1px solid var(--ink); }

  .tuck-bottom { left: 701px; top: 958px; width: 172px; }
  .tuck-bottom .brand-name { font-size: 20px; line-height: 1.1; }
</style>
</head>
<body>
<main class="artboard">
  <svg class="dieline" width="1143" height="1200" viewBox="0 0 1143 1200" aria-hidden="true">
    <g fill="var(--panel)" stroke="var(--cut)" stroke-width="1.5" stroke-linejoin="round">
      <polygon points="190,327 190,302 201,291 214,241 337,241 341,311 358,327"/>
      <polygon points="530,327 547,312 553,241 675,241 689,291 700,302 700,327"/>
      <polygon points="188,870 204,885 210,955 332,955 345,905 356,894 356,870"/>
      <polygon points="531,870 531,894 544,905 556,955 678,955 684,887 700,871"/>
      <path d="M361,161 V127 A83.5,83.5 0 0 1 528,127 V161 Z" fill="var(--tuck)"/>
      <polygon points="358,155 390,155 395,161 497,161 502,155 530,155 530,327 358,327"/>
      <path d="M703,1039 V1073 A84,84 0 0 0 871,1073 V1039 Z" fill="var(--tuck)"/>
      <polygon points="701,871 873,871 873,1045 843,1045 838,1039 736,1039 731,1045 701,1045"/>
      <polygon points="873,327 960,341 960,856 873,870"/>
      <rect x="188" y="327" width="685" height="543"/>
    </g>
    <g stroke="var(--fold)" stroke-width="0.8" opacity="0.8">
      <line x1="190" y1="327" x2="873" y2="327"/>
      <line x1="188" y1="870" x2="873" y2="870"/>
    </g>
    <g stroke="#2a2f31" stroke-width="1">
      <line x1="358" y1="327" x2="358" y2="870"/>
      <line x1="530" y1="327" x2="530" y2="870"/>
      <line x1="701" y1="327" x2="701" y2="870"/>
      <line x1="873" y1="327" x2="873" y2="870"/>
    </g>
  </svg>

  <div class="panel-text tuck-top"><div class="brand-name">Dusk<br>Haven</div></div>

  <section class="panel-text ingredients">
    <h3>INGREDIENTS:</h3>
    <p>Lavandula Angustifolia (Australian Lavender), Vetiveria Zizanoides (Vetiver) Root Oil, Sweet Vanilla Fragrant Oil, Pelargonium Capitatum (Cape Rose Geranium) Leaf Extract, Juniperus Virginiana (Cedarwood) Wood Oil, Citrus Limon (Australian Lemon) Peel Oil, Origanum Majorana (Marjoram) Leaf Oil, Cananga Odorata (Ylang Ylang) Flower Oil, Anthemis Nobilis (Roman Chamomile) Flower Oil</p>
  </section>
  <svg class="care-icons" viewBox="0 0 150 56" role="img" aria-label="Recyclable and 12 month period after opening symbols" fill="none" stroke="var(--ink)" stroke-width="1.3" stroke-linejoin="round">
    <path d="M22,6 L30,6 L36,16 L40,14 L38,24 L29,22 L33,20 L28,12 L24,12 Z"/>
    <path d="M42,30 L46,37 L42,45 L32,45 L32,49 L25,42 L32,35 L32,39 L39,39 L37,34 Z"/>
    <path d="M18,45 L9,45 L5,37 L10,28 L6,26 L16,24 L19,33 L15,31 L12,37 L16,40 Z"/>
    <path d="M88,18 L117,2 L120,6 L91,22 Z"/>
    <ellipse cx="112" cy="32" rx="18" ry="4"/>
    <path d="M94,32 V48 A18,4 0 0 0 130,48 V32"/>
  </svg>

  <div class="panel-text front-brand"><div class="brand-name">Dusk<br>Haven</div></div>
  <div class="panel-text product-line">
    <div class="roll">Roll on</div>
    <div>Essential Oil Blend</div>
  </div>
  <div class="front-photo" role="img" aria-label="Black and white photograph of a mother and child sleeping peacefully in bed"></div>
  <div class="front-band">Made in Australlia<br>15ml</div>

  <div class="direction inhale"><h4>Inhale</h4>Place 2 drops in the palms of<br>the hands and inhale directly to<br>ease you into a restful sleep</div>
  <div class="direction diffuse"><h4>Diffuse</h4>Add 4-6 drops to a diffuser or<br>oil burner at night to create a<br>calm and grounded<br>environment.</div>
  <div class="direction bathe"><h4>Bathe</h4>Add 2-4 drops to a warm bath<br>to help calm the body and mind</div>
  <div class="direction massage"><h4>Massage</h4>Dilute 4 drops with a carrier oil<br>(such as jojoba or coconut), and<br>massage into the feet before<br>sleep</div>
  <p class="panel-text caution">Caution:<br>Possible skin sensitivity. Keep out of reach of children. Not for ingestion or internal use. Avoid contact with eyes, inner ears and sensitive areas.</p>

  <section class="panel-text about">
    <p>Essential Oils have been used for centuries to help prepare the mind and body for sleep</p>
    <hr>
    <p>Dusk Haven contain a balanced blend of the most sleep supporting essential oils, renowned for their grounding and calming properties.</p>
    <hr>
    <p><b>Lavender</b> for restfulness<br><b>Vetiver</b> for grounding<br><b>Cedarwood</b> for relaxation<br><b>Marjoram</b> for balance<br><b>Roman Chamomile</b> for comfort</p>
    <hr>
    <p>Add Dusk Haven to your nightly bedtime ritual to help support you in achieving deep and rejuvenating sleep</p>
    <hr>
    <p class="visit">Visit <a href="#">www.duskhaven.com.au</a><br>to learn more</p>
    <p class="social"><span class="dot"></span> | @duskhavenau</p>
  </section>

  <div class="panel-text tuck-bottom"><div class="brand-name">Dusk<br>Haven</div></div>
</main>
</body>
</html>
```